3 Politically Incorrect Greeting Cards

I would like to see some clean, colorful, and modern designs for 3 "politically incorrect" greeting cards aimed at young, single, successful women. I would like them to say:

Card 1: " Congratulations on not marrying the wrong person"
Card 2: " Congratulations on buying a house without a husband"
Card 3: " Thank you for not forgetting about me now that you have a boyfriend"

My initial thought was to have a white background with simple black writing, but I think a colorful background with a white text box in the middle might be more appropriate. I can't imagine the cards having any images/icons on them, but I'm open to suggestions if you think it would improve on the design. You guys are likely more creative than I am.

I've included a couple pics of looks I like - but like I said - I'm open to suggestions and what I like may not be appropriate for these cards. All the cards can have a similar esthetic or theme (maybe the same fonts but different colors or different color florals in each) or they can be completely different.

Target Market(s)

Young, single, successful women mid-20s to mid 40's.

Font styles to use
Serif
Sans Serif
Other font styles liked:
• Watercolour lettering maybe

Colors

Designer to choose colors to be used in the design.

Requirements
Must have
• Clean, colorful, bright, professional looking. The right tone for the message.
• I think the message is bold so the writing and colors have to be as well. I have included examples of ideas I like.
Nice to have
• Images, illustrations, icons, maybe patterns or some decorative details. Something to make the card more interesting than just the words (like the blue background with black letters one I made). I like a bright pattern with a white box in the center with the text.
Should not have
• Special effects, galaxy pictures, ugly images, bland colors.

```html
<!DOCTYPE html>
<html lang="en">
<head>
<meta charset="utf-8">
<title>Congratulations Card</title>
<link rel="stylesheet" href="https://fonts.googleapis.com/css2?family=Amatic+SC:wght@400;700&display=swap">
<style>
  :root {
    --backdrop-pink: #fcc8cb;
    --card-white: #ffffff;
    --ink: #111111;
    --mint-dot: #7fe3c9;
    --card-shadow: rgba(40, 20, 20, 0.55);
  }
  * { margin: 0; padding: 0; box-sizing: border-box; }
  html, body {
    width: 1200px;
    height: 1200px;
    overflow: hidden;
    background: var(--backdrop-pink);
  }
  .canvas {
    position: relative;
    width: 1200px;
    height: 1200px;
    background: var(--backdrop-pink);
  }
  .card {
    position: absolute;
    left: 45px;
    top: 203px;
    width: 1113px;
    height: 784px;
    background: var(--card-white);
    box-shadow: 3px 3px 3px var(--card-shadow);
    display: flex;
    align-items: center;
    justify-content: center;
  }
  .corner-dot {
    position: absolute;
    width: 32px;
    height: 34px;
    border-radius: 50%;
    background: radial-gradient(circle at 45% 45%, #9aeed8 0%, var(--mint-dot) 70%, #6fd9be 100%);
    opacity: 0.9;
  }
  .corner-dot.top-left { left: 68px; top: 69px; }
  .corner-dot.top-right { left: 1013px; top: 69px; }
  .corner-dot.bottom-left { left: 68px; top: 680px; }
  .corner-dot.bottom-right { left: 1013px; top: 680px; }
  .message {
    display: flex;
    flex-direction: column;
    align-items: center;
    font-family: "Amatic SC", cursive;
    font-weight: 400;
    font-size: 92px;
    line-height: 116px;
    letter-spacing: 1px;
    color: var(--ink);
    text-transform: uppercase;
    text-align: center;
  }
  .message-line { display: block; white-space: nowrap; }
</style>
</head>
<body>
  <main class="canvas">
    <section class="card">
      <span class="corner-dot top-left"></span>
      <span class="corner-dot top-right"></span>
      <span class="corner-dot bottom-left"></span>
      <span class="corner-dot bottom-right"></span>
      <h1 class="message">
        <span class="message-line">Congratulations</span>
        <span class="message-line">on buying a house</span>
        <span class="message-line">without</span>
        <span class="message-line">a husband</span>
      </h1>
    </section>
  </main>
</body>
</html>
```